Anzeigengestaltung für KFZ-Werkstatt
Zielgruppe
Wir sind eine KFZ-Werkstatt mit vielumfänglichen Dienstleistungen. Unsere Zielgruppe beschränkt sich auf einen Umkreis von ca. 10km. Wir bieten alles rund ums KFZ: Service, Inspektion, Reparaturen aller Art, TÜV, Rad/Reifen/Felgen, Spurvermessung, Unfallinstandsetzung.
Aufgabenstellung
wir nutzen den Hashtag '#autowelmsdorn' für Werbung im Internet sowie in den Werbeanzeigen. Wir verwenden diesen 'Slogan' in der SChriftart 'Hashtag', diese kann überall runtergeladen werden. dieser muss in den Werbeanzeigen nicht im Vordergrund stehen, da hier die Zielgruppe eher in Richtung 40+ geht.
es muss auch Platz für die offizielle Firmierung samt Anschrift, Telefon und Internet sein (kein Fax).
was die Anzeige an sich angeht, so sollte das Motiv (gerne erst mal einfach ein Stockfoto) durch uns austauschbar sein. Sprich: wenn Reifensaison ist, wollen wir da ein eigenes Motiv reinstecken können; im Sommer wiederum ein anderes etc. Zudem verwenden wir auch Standardfotos von unserem Unternehmen, welches wir platzieren lassen wenn ein Monat mal nichts besonderes ansteht (die Werbung wird monatlich geschaltet).
Maße: 172x100mm
Hauptfarben (bedingt durch das System, an das wir angeschlossen sind):
ROT: C15 M100 Y100 K0 (oder HKS15; oder Pantone 1797)
GRAU: C0 M0 Y0 K50 (oder 50% HKS90; oder Pantone Cool Gray 7)
Aufgrund der Zielgruppe haben wir als Wunsch 'erschwinglich' angegeben. Dies soll aber nicht heißen, dass wir nicht bereit sind, für das Erstellen der Anzeige kein Geld auszugeben. Nein, damit wollen wir unterstreichen, dass es nicht irre aufgepusht sein soll mit wahnsinns-Effekten etc.

```html
<!DOCTYPE html>
<html lang="de">
<head>
<meta charset="utf-8">
<title>KFZ Brandl &amp; Hohenwarter – Anzeige</title>
<link rel="stylesheet" href="https://fonts.googleapis.com/css2?family=PT+Sans:wght@400;700&family=PT+Sans+Narrow:wght@700&display=swap">
<style>
  :root {
    --red: #d3202c;
    --rule: #e3636b;
    --white: #ffffff;
    --visual-dark: #3c3d41;
    --visual-light: #8d8f94;
  }
  html, body {
    margin: 0;
    padding: 0;
    width: 1200px;
    height: 696px;
    overflow: hidden;
    background: var(--red);
  }
  .ad {
    position: relative;
    width: 1200px;
    height: 696px;
    background: var(--red);
    font-family: "PT Sans", Arial, sans-serif;
    color: var(--white);
    overflow: hidden;
  }
  .ad__rule {
    position: absolute;
    left: 0;
    width: 1200px;
    height: 3px;
    background: var(--rule);
  }
  .ad__rule--top { top: 72px; }
  .ad__rule--bottom { top: 596px; }
  .ad__visual {
    position: absolute;
    left: 636px;
    top: 30px;
    width: 610px;
    height: 640px;
    border-radius: 50%;
    background: linear-gradient(135deg, var(--visual-light) 0%, var(--visual-dark) 100%);
  }
  .ad__headline {
    position: absolute;
    left: 64px;
    top: 84px;
    margin: 0;
    font-size: 80px;
    line-height: 98px;
    font-weight: 700;
    letter-spacing: 0.5px;
    text-transform: uppercase;
  }
  .ad__pointer {
    position: absolute;
    left: 44px;
    top: 294px;
    width: 620px;
    height: 42px;
  }
  .ad__services {
    position: absolute;
    left: 66px;
    top: 340px;
    margin: 0;
    font-size: 29px;
    line-height: 39px;
    font-weight: 400;
  }
  .ad__cta {
    position: absolute;
    left: 66px;
    top: 515px;
    margin: 0;
    font-family: "PT Sans Narrow", "PT Sans", Arial, sans-serif;
    font-size: 32px;
    line-height: 40px;
    font-weight: 700;
  }
  .ad__footer {
    position: absolute;
    left: 66px;
    right: 66px;
    top: 619px;
    margin: 0;
    display: flex;
    justify-content: space-between;
    font-size: 18px;
    line-height: 26px;
  }
  .ad__footer .sep {
    display: inline-block;
    width: 2px;
    height: 16px;
    margin: 0 7px -2px;
    background: var(--white);
  }
</style>
</head>
<body>
  <div class="ad">
    <div class="ad__rule ad__rule--top"></div>
    <div class="ad__visual" role="img" aria-label="Austauschbares Motiv: Foto eines Autoreifens mit Alufelge"></div>

    <h1 class="ad__headline">Time for<br>a change!</h1>

    <svg class="ad__pointer" viewBox="0 0 620 42" aria-hidden="true">
      <line x1="0" y1="21" x2="600" y2="21" stroke="#ffffff" stroke-width="4"/>
      <circle cx="600" cy="21" r="17" fill="#ffffff"/>
    </svg>

    <p class="ad__services">
      Wir kümmern uns um allgemeine<br>
      KFZ Services, Inspektionen, TÜV,<br>
      Reparaturen, Rad/Reifen/Felgen,<br>
      Spurvermessung, Unfallinstandsetzung
    </p>

    <p class="ad__cta">Kontaktieren Sie uns noch heute!</p>

    <div class="ad__rule ad__rule--bottom"></div>

    <p class="ad__footer">
      <span class="ad__address">KFZ Brandl &amp; Hohenwarter<span class="sep"></span>Donaustrasse 17<span class="sep"></span>T: 09471 3820<span class="sep"></span>info@kfz-welmsdorn.de</span>
      <span class="ad__hashtag">#autowelmsdorn</span>
    </p>
  </div>
</body>
</html>
```